Quorvane Capital Modern Business Card

We need a modern business card template designed for Quorvane Capital.
Quorvane Capital is a diversified global cryptocurrency investment fund.

The font under the logo: Hiragino Kaku Gothic Pro

Color Hexcode: Main colors white (ffffff) & teal (188383), we are open to adding #fcca46 as an accent

Target Market(s)

Accredited Investors, high net worth individuals and institutional investors

Industry/Entity Type

Investment

Contact Information for Business Card

Contact Information should contain
Name
main phone +1 720 555 0147
cell
email

Font styles to use
Sans Serif
Other font styles liked:
• Hiragino Kaku Gothic Pro

Requirements
Must have
• would like to have icons that identify the contact information
• include our website: www.quorvanecapital.example
• include our Tagline: Diversified Crypto Investment Funds
Nice to have
• Would like to have a simple back side with the logo (without the words) and plenty of space

```html
<!DOCTYPE html>
<html lang="en">
<head>
<meta charset="utf-8">
<title>Quorvane Capital Business Card</title>
<link rel="stylesheet" href="https://fonts.googleapis.com/css2?family=Open+Sans:ital,wght@0,400;0,700;1,700&display=swap">
<style>
  :root {
    --backdrop: #f3f3f1;
    --card: #000000;
    --text: #ffffff;
    --teal: #188383;
    --accent: #fcca46;
  }
  * { margin: 0; padding: 0; box-sizing: border-box; }
  html, body {
    width: 1200px; height: 1000px; overflow: hidden;
    background: var(--backdrop);
    font-family: "Open Sans", Arial, sans-serif;
    color: var(--text);
  }
  .canvas { position: relative; width: 1200px; height: 1000px; }
  .card {
    position: absolute;
    background: var(--card);
    border-radius: 34px;
    overflow: hidden;
  }
  .card--front { left: 257px; top: 72px; width: 688px; height: 395px; }
  .card--back  { left: 257px; top: 527px; width: 686px; height: 392px; }

  .identity {
    position: absolute; left: 33px; top: 35px;
    padding-left: 16px;
    border-left: 6px solid var(--accent);
    height: 76px;
  }
  .identity__name { font-size: 26px; font-weight: 700; line-height: 1; margin-top: 12px; letter-spacing: 0.5px; }
  .identity__role { font-size: 18px; font-weight: 400; line-height: 1; margin-top: 6px; }

  .company-info { position: absolute; left: 33px; top: 196px; }
  .company-info__web { font-size: 16px; line-height: 22px; }
  .company-info__tagline { font-size: 16px; font-weight: 700; font-style: italic; line-height: 22px; margin-top: 6px; }

  .brand {
    position: absolute; left: 420px; top: 68px; width: 250px;
    display: flex; flex-direction: column; align-items: center;
  }
  .brand__mark { width: 74px; height: 74px; background: var(--teal); margin-bottom: 88px; }
  .brand__name { font-size: 24px; font-weight: 400; letter-spacing: 0.5px; line-height: 1; white-space: nowrap; }

  .contacts { position: absolute; left: 0; top: 301px; width: 100%; }
  .contact {
    position: absolute; top: 0; width: 240px;
    display: flex; flex-direction: column; align-items: center;
  }
  .contact--phone { left: -19px; }
  .contact--email { left: 223px; }
  .contact--mobile { left: 466px; }
  .contact__icon { width: 32px; height: 32px; }
  .contact__text { font-size: 17px; line-height: 1; margin-top: 15px; white-space: nowrap; }

  .accent-strip { position: absolute; right: 0; bottom: 0; width: 220px; height: 18px; }

  .back-brand {
    position: absolute; left: 0; top: 0; width: 100%; height: 100%;
    display: flex; flex-direction: column; align-items: center; justify-content: center;
  }
  .back-brand__mark { width: 60px; height: 60px; border-radius: 50%; background: var(--teal); margin-bottom: 22px; }
  .back-brand__name { font-size: 24px; font-weight: 400; letter-spacing: 1px; color: var(--teal); }
</style>
</head>
<body>
<div class="canvas">

  <section class="card card--front" aria-label="Business card front">
    <div class="identity">
      <p class="identity__name">JOHN DOE</p>
      <p class="identity__role">Manager</p>
    </div>

    <div class="company-info">
      <p class="company-info__web">www.quorvanecapital.example</p>
      <p class="company-info__tagline">Diversified Crypto Investment Funds</p>
    </div>

    <div class="brand">
      <div class="brand__mark"></div>
      <p class="brand__name">QUORVANE CAPITAL</p>
    </div>

    <div class="contacts">
      <div class="contact contact--phone">
        <svg class="contact__icon" viewBox="0 0 32 32" aria-hidden="true">
          <circle cx="16" cy="16" r="16" fill="var(--teal)"/>
          <path d="M11.5 8.5l2.6 0 1.2 3.6-1.7 1.3c.8 1.9 2.3 3.4 4.2 4.2l1.3-1.7 3.6 1.2 0 2.6c0 .9-.8 1.7-1.7 1.6-5.4-.4-9.7-4.7-10.1-10.1-.1-.9.7-1.7 1.6-1.7z" fill="#fff"/>
        </svg>
        <p class="contact__text">+1 720 555 0147</p>
      </div>
      <div class="contact contact--email">
        <svg class="contact__icon" viewBox="0 0 32 32" aria-hidden="true">
          <circle cx="16" cy="16" r="16" fill="var(--teal)"/>
          <rect x="8.5" y="11" width="15" height="10.5" rx="1" fill="none" stroke="#fff" stroke-width="1.6"/>
          <path d="M9 11.8l7 5.2 7-5.2" fill="none" stroke="#fff" stroke-width="1.6"/>
        </svg>
        <p class="contact__text">email@quorvanecapital.example</p>
      </div>
      <div class="contact contact--mobile">
        <svg class="contact__icon" viewBox="0 0 32 32" aria-hidden="true">
          <circle cx="16" cy="16" r="16" fill="var(--teal)"/>
          <rect x="11.5" y="7.5" width="9" height="17" rx="1.5" fill="none" stroke="#fff" stroke-width="1.6"/>
          <rect x="14.5" y="21.2" width="3" height="1.2" fill="#fff"/>
        </svg>
        <p class="contact__text">+1 720 555 0192</p>
      </div>
    </div>

    <svg class="accent-strip" viewBox="0 0 220 18" preserveAspectRatio="none" aria-hidden="true">
      <polygon points="10,0 220,0 220,18 0,18" fill="var(--accent)"/>
    </svg>
  </section>

  <section class="card card--back" aria-label="Business card back">
    <div class="back-brand">
      <div class="back-brand__mark"></div>
      <p class="back-brand__name">QUORVANE CAPITAL</p>
    </div>
  </section>

</div>
</body>
</html>
```